Seedline Ventura high class WEBSITE to entice accredited investors to take a look at our servics

I want a FULLY FUNCTIONAL SITE and I'm willing to pay. I've made this a GUARANTEED project and I'm adding funding to entice you shit hot designers to get on this!
I expect a Web Site with approx 5-6 HTML pages with full navigation AND 4 simple FORMS that function. Nothing tricky. We will provide our hosting server password, etc when the design is complete. The site will have to be fully functional, as per my approval. I'm easy to deal with, pay my bills and have a shit ton of future work for a great designer. I'm not kidding. Now get to work!

BadAss cutting edge Web Site for a BadAss cutting edge company. We want the investment class to take a look at the projects we are developing in the new GREEN WAVE cannabis industry. There are so many opportunities to invest. We also want current professional growers to know they can turn to us for help with the management of their farms/grows.

Target Market(s)

Accredited investors. Upscale. Easy to navigate.

Coding

Coded - Design and coding required

Number of Pages Required

5+ page

Requirements
Must have
• USE MY LOGO! its AWESOME! Logo provided. Marijuana/cannabis leaf should be incorporated.
• Im trying to run an awesome company, travel and create content for the site all at the same time. I'm sorry if it is not as neatly delivered as you normally expect. This is the only place I know where I can get the content to you designers. I will know the design I want when I see it. I LOVE our logo and our trade show booth which is attached. I will attach my business card as well. Bring in the cannabis leaves, high tech growing facilities, laboratory pics, etc. We will provide nice pics when we come to a decision on a designer for the web site. We will be purchasing several other businesses so we'll have more work for you.
• Home page
• (LINKS)
• What we do
• Who we are
• Contact us
• Sample projects
• Accredited Investors
• Farm Efficiency
• Trade show schedule
• I will provide content.
• Navigation bar should be available at top and bottom of each sub page.
• content notes to date.......
• HOME PAGE – Logo, marijuana plants, “Invest, Manage, Innovate”
• Services
• Seedline Ventura created a system to bring investors and qualified professional growers together.
• Many, from both the investment and growing sides, come into the cannabis industry under-educated and/or underfunded, leading to disappointing failure.
• Seedline Ventura brings the proper funding, award winning cannabis cultivation, custom genetic creation, cost saving technologies and proven business practices to help our clients become more efficient and profitable.
• Leadership
• Gavin Thorley, the brains. Concepter in Chief
• Ross Dabney, the brawn. Harvester General
• Sample projects
• Quiet Brook Farm
• SilverPine Dispensary
• 4 pals and a totally odd pal Genetics
• Trade show schedule
• Contact Us
• Forms
• Accredited Investors – Are you an accredited investor* looking to enter the exciting GREEN RUSH?
• Invest – We introduce accredited investors to qualified investments in the cannabis industry. Both investors AND opportunities are vetted to our high standards ensuring a higher probability of success.
• If you are an accredited investor, please complete the form below and we will be in touch. Your information will NEVER be shared without YOUR permission.
• *In the United States, to be considered an accredited investor, one must have a net worth of at least $1,000,000, excluding the value of one's primary residence, or have income at least $200,000 each year for the last two years (or $300,000 combined income if married) and have the expectation to make the same amount this year. The term "accredited investor" is defined in Rule 501 of Regulation D of the U.S. Capital and Markets Oversight Bureau (CMOB) as:
• a bank, insurance company, registered investment company, business development company, or small business investment company;
• an employee benefit plan, within the meaning of the Employee Retirement Income Security Act, if a bank, insurance company, or registered investment adviser makes the investment decisions, or if the plan has total assets in excess of $5 million;
• a charitable organization, corporation, or partnership with assets exceeding $5 million;
• a director, executive officer, or general partner of the company selling the securities;
• a business in which all the equity owners are accredited investors;
• a natural person who has individual net worth, or joint net worth with the person's spouse, that exceeds $1 million at the time of the purchase, or has assets under management of $1 million or above, excluding the value of the individual's primary residence;[11][12]
• a natural person with income exceeding $200,000 in each of the two most recent years or joint income with a spouse exceeding $300,000 for those years and a reasonable expectation of the same income level in the current year;[13] or
• a trust with assets in excess of $5 million, not formed to acquire the securities offered, whose purchases a sophisticated person makes."[14][15]
• [11] CMOB Tightens Rules on Advisory Performance Fee Charges
• [12] Enterprise Equity Counsel Journal: Legal Update: Garvin-Holt Redefines "Accredited Investor"
• [13] Pryce, Daniel; Hartwell and Soto LLP (March 6, 2013). "Raising Capital - [14] What You Don't Know Could Hurt You". The [Federal Legal Digest]. Retrieved March 26, 2013.
• [15] U.S. Capital and Markets Oversight Bureau on Accredited Investors
• 17 C.F.R. sec. 230.501(a).
• First name Last name
• Email Phone Country of residence
• Is there a specific category in the Cannabis Industry you have a passion for?
• Industrial Indoor grow Industrial outdoor grow genetics maintenance testing dispensary medical CBD recreational THC transport banking any of the above
• What amount of investment are you looking to make?
• What are your expectations?
• Do you currently possess a cannabis license of any kind?
• Are you on any waiting lists to receive a cannabis license of any kind?
• Cannabusiness Owners – Are you the owner or manager of a cannabusiness looking for help to become profitable and more efficient?
• What type of business do you operate?
• Industrial Indoor grow Industrial outdoor grow genetics maintenance testing dispensary medical CBD recreational THC transport banking other________
• General questions – Please fill out the form and submit.
• Name email Phone Message
Nice to have
• Small window with rotating pictures we will provide.

```html
<!DOCTYPE html>
<html lang="en">
<head>
<meta charset="utf-8">
<title>Seedline Ventura — Get in Touch</title>
<link rel="stylesheet" href="https://fonts.googleapis.com/css2?family=Poppins:wght@400;500;600&display=swap">
<style>
  :root {
    --ink: #1d1d1d;
    --navy: #0d2a5c;
    --brand-green: #1f6b35;
    --button-blue: #4a63c7;
    --field: #ececec;
    --modal-bg: #f7f7f7;
    --placeholder: #5d6a4a;
    --page: #f4f4f4;
    --card: #ffffff;
    --side-mail: #1e8c4e;
    --side-info: #1a9a8c;
    --side-share: #1b3a9c;
    --dim: rgba(0, 0, 0, 0.72);
  }
  * { box-sizing: border-box; margin: 0; padding: 0; }
  html, body { width: 1200px; height: 766px; overflow: hidden; }
  body { position: relative; font-family: "Poppins", sans-serif; background: var(--page); color: var(--ink); }

  .hero-photo {
    position: absolute; left: 0; top: 0; width: 1200px; height: 531px;
    background: linear-gradient(120deg, #8d8f86 0%, #b9bcb3 35%, #6f7568 70%, #9ea393 100%);
  }
  .site-header {
    position: absolute; left: 0; top: 0; width: 1200px; height: 79px;
    background: rgba(255, 255, 255, 0.3);
  }
  .brand { position: absolute; left: 64px; top: 24px; display: flex; align-items: center; gap: 8px; }
  .brand-dot { width: 26px; height: 26px; border-radius: 50%; background: var(--brand-green); }
  .brand-name { font-size: 24px; font-weight: 600; color: var(--brand-green); }
  .main-nav { position: absolute; left: 338px; top: 39px; display: flex; gap: 23px; }
  .main-nav a { font-size: 12px; font-weight: 500; color: #ffffff; text-decoration: none; }
  .lang { position: absolute; left: 1040px; top: 10px; display: flex; align-items: center; gap: 6px; font-size: 8px; font-weight: 600; color: #fff; }
  .lang-dot { width: 12px; height: 12px; border-radius: 50%; background: #c8465a; }
  .header-cta {
    position: absolute; left: 1012px; top: 30px; width: 117px; height: 31px; border-radius: 16px;
    background: var(--side-share); color: #fff; font-size: 9px; font-weight: 600;
    display: flex; align-items: center; justify-content: center;
  }
  .side-tabs { position: absolute; left: 1160px; top: 127px; display: flex; flex-direction: column; gap: 12px; }
  .side-tab { width: 48px; height: 35px; border-radius: 18px 0 0 18px; display: flex; align-items: center; padding-left: 14px; }
  .side-tab.mail { background: var(--side-mail); }
  .side-tab.info { background: var(--side-info); }
  .side-tab.share { background: var(--side-share); }

  .contact-card { position: absolute; left: 143px; top: 442px; width: 914px; height: 180px; background: var(--card); }
  .contact-title { position: absolute; left: 108px; top: 49px; font-size: 19px; font-weight: 600; }
  .contact-line { position: absolute; font-size: 11px; color: #333; }

  .dim-layer { position: absolute; inset: 0; background: var(--dim); }

  .close-btn { position: absolute; left: 1134px; top: 43px; }

  .contact-modal {
    position: absolute; left: 401px; top: 172px; width: 398px; height: 469px;
    background: var(--modal-bg); box-shadow: 0 4px 18px rgba(0,0,0,0.3);
  }
  .modal-title { position: absolute; top: 36px; width: 100%; text-align: center; font-size: 30px; font-weight: 600; color: var(--navy); }
  .field {
    position: absolute; left: 44px; width: 312px; height: 38px; background: var(--field);
    font-size: 11px; color: var(--placeholder); display: flex; align-items: center; padding-left: 23px;
  }
  .field.select { padding-left: 26px; color: #3b5a74; }
  .field.select svg { position: absolute; right: 20px; top: 14px; }
  .submit-btn {
    position: absolute; left: 140px; top: 389px; width: 118px; height: 40px; border-radius: 20px;
    background: var(--button-blue); color: #fff; font-size: 11px; font-weight: 500;
    display: flex; align-items: center; justify-content: center;
  }
</style>
</head>
<body>
  <div class="hero-photo" role="img" aria-label="Desk scene with a potted plant, laptop and leafy greenery"></div>

  <header class="site-header">
    <div class="brand"><span class="brand-dot"></span><span class="brand-name">Seedline Ventura</span></div>
    <nav class="main-nav">
      <a href="#">Home</a><a href="#">Who We Are</a><a href="#">What We Do</a>
      <a href="#">Sample Projects</a><a href="#">Invest</a><a href="#">Trade Show Schedule</a>
    </nav>
    <div class="lang"><span class="lang-dot"></span>ENGLISH</div>
    <div class="header-cta">GET IN TOUCH</div>
  </header>

  <div class="side-tabs">
    <div class="side-tab mail"><svg width="14" height="10" viewBox="0 0 14 10"><rect width="14" height="10" fill="#fff"/><path d="M0 0 L7 6 L14 0" stroke="#1e8c4e" fill="none"/></svg></div>
    <div class="side-tab info"><svg width="12" height="12" viewBox="0 0 12 12"><circle cx="6" cy="6" r="6" fill="#fff"/><rect x="5.2" y="5" width="1.6" height="4.5" fill="#1a9a8c"/><circle cx="6" cy="3.3" r="0.9" fill="#1a9a8c"/></svg></div>
    <div class="side-tab share"><svg width="12" height="12" viewBox="0 0 12 12"><path d="M9 2 L3 6 L9 10" stroke="#fff" stroke-width="1.3" fill="none"/><circle cx="9.5" cy="2" r="2" fill="#fff"/><circle cx="2.5" cy="6" r="2" fill="#fff"/><circle cx="9.5" cy="10" r="2" fill="#fff"/></svg></div>
  </div>

  <section class="contact-card">
    <h3 class="contact-title">Call</h3>
    <p class="contact-line" style="left:108px;top:89px">312 555 0147</p>
    <p class="contact-line" style="left:108px;top:117px">312 555 0193</p>
    <p class="contact-line" style="left:600px;top:90px">info@seedline.com</p>
    <p class="contact-line" style="left:600px;top:167px">invest@seedline.com</p>
  </section>

  <div class="dim-layer"></div>

  <svg class="close-btn" width="22" height="22" viewBox="0 0 22 22" aria-label="Close">
    <path d="M3 3 L19 19 M19 3 L3 19" stroke="#fff" stroke-width="3.5" stroke-linecap="round"/>
  </svg>

  <form class="contact-modal">
    <h2 class="modal-title">Get in Touch</h2>
    <div class="field select" style="top:101px">Reason for Contacting
      <svg width="12" height="8" viewBox="0 0 12 8"><path d="M1 1 L6 6 L11 1" stroke="#999" stroke-width="1.2" fill="none"/></svg>
    </div>
    <div class="field" style="top:155px">Name</div>
    <div class="field" style="top:210px">Company</div>
    <div class="field" style="top:265px">Contact No.</div>
    <div class="field" style="top:319px">Email</div>
    <div class="submit-btn">Submit</div>
  </form>
</body>
</html>
```